Vel Tor Concrete Post Card Design Project

Hello, We are A Concrete Contractor. We specialize in removing and replacing concrete walkways, Patio's, Driveway's, ect., that are a trip hazard. We work a lot in Apartment complexes and Business Complexes where the trees have grown big and the roots from the trees lift up the concrete.
I would like someone to design a postcard (Two Sided) so I can send it out and market potential property manager customers. I would like to use our company logo on this card. Please see the snap vault link below. Here are some things I would like the card to have on it.

1.Removal and Replacement of Concrete Sidewalks, Driveways, Parking Lots, Curb and Gutter.

2. ADA Compliant.

3. Repair of concrete tripping hazards and
root-damaged sidewalks.

4. Vel Tor Concrete brings your sidewalks in compliance with the Americans With Disabilities Act (ADA).

5. Property Management:

We cater to the needs of Property Mangement Companies, HOA, Apartment Complexes, Business Parks, Senior Living Complexes, Government Buildings and Shopping Centers.

6. Free Estimates
7. Contractors license number under our logo. It is:
RBQC #318907
8. Our phone numbers:530-842-1964 and 530-729-6350.

Card should be two sided 9" by 6"

Thank You
Updates

This website would not let me upload my logo so please click on the link below to get it.

 

http://img4471.snapvaultpix.net/albums/k302/Jvelt42/VelTorConcreteLogo-2012-PROOF-2.jpg

Thank You

Reason: Hello, I have a lot of great designs. I have had a busy week and I am just now sitting down to ask for the changes I would like. Once I recieve all of the designs back with the changes I requested I would like to get the opinions of my coworkers and friends before selecting the design. I am asking for the deadline to be extended by 4 days. Thank You so much, Janice Vel Tor

Target Market(s)

Property Managers

Industry/Entity Type

Concrete

Requirements
Must have
• Our logo

```html
<!DOCTYPE html>
<html lang="en">
<head>
<meta charset="utf-8">
<title>Vel Tor Concrete Postcard</title>
<link href="https://fonts.googleapis.com/css2?family=Nunito+Sans:wght@400;700&display=swap" rel="stylesheet">
<style>
  :root {
    --backdrop: #ececec;
    --card: #ffffff;
    --ink: #1a1a1a;
    --sketch-dark: #c4c4c4;
    --sketch-light: #f2f2f2;
    --shadow: rgba(70, 60, 110, 0.35);
  }
  html, body {
    margin: 0;
    width: 1200px;
    height: 1000px;
    overflow: hidden;
    background: var(--backdrop);
  }
  .postcard {
    position: absolute;
    left: 120px;
    top: 157px;
    width: 960px;
    height: 686px;
    background: var(--card);
    box-shadow: 3px 4px 6px var(--shadow);
    overflow: hidden;
    font-family: "Nunito Sans", sans-serif;
    color: var(--ink);
  }
  .scene-art {
    position: absolute;
    inset: 0;
    background:
      radial-gradient(ellipse 230px 190px at 760px 175px, var(--sketch-dark), rgba(255,255,255,0) 100%),
      linear-gradient(180deg, rgba(255,255,255,0) 40%, var(--sketch-light) 60%, rgba(255,255,255,0) 100%);
  }
  .brand {
    position: absolute;
    left: 40px;
    top: 50px;
    margin: 0;
    font-weight: 700;
    font-size: 62px;
    line-height: 1.05;
    color: var(--ink);
  }
  .services {
    position: absolute;
    right: 27px;
    top: 360px;
    width: 880px;
    text-align: right;
  }
  .service-title {
    margin: 0;
    font-weight: 700;
    font-size: 20px;
    line-height: 1.3;
  }
  .service-text {
    margin: 0;
    font-size: 14.5px;
    line-height: 1.45;
  }
  .gap-sm { margin-bottom: 22px; }
  .gap-md { margin-bottom: 28px; }
  .gap-lg { margin-bottom: 44px; }
</style>
</head>
<body>
  <main class="postcard">
    <div class="scene-art" role="img" aria-label="Faint gray sketch of a large tree beside a walkway and railing"></div>

    <h1 class="brand">Vel Tor<br>Concrete</h1>

    <section class="services">
      <h2 class="service-title">Removal and Replacement:</h2>
      <p class="service-text gap-sm">Concrete Sidewalks, Driveways, Parking Lots, Curb and Gutters and ADA Compliant.</p>

      <h2 class="service-title">Concrete Grinding:</h2>
      <p class="service-text gap-md">Repair of tripping hazard removal, root-damaged sidewalks, 24 Hr Service.</p>

      <p class="service-text gap-lg">Vel Tor Concrete brings your sidewalks in compliance with the Americans With Disabilities Act (ADA).</p>

      <h2 class="service-title">Property Management:</h2>
      <p class="service-text">We cater to the needs of Property Mangement Companies,<br>
      HOA, Apartment Complexes, Business Parks, Senior Living Complex, Government Buildings and Shopping Centers,<br>
      concrete trip hazard repair and removal, sidewalk concrete repair.</p>
    </section>
  </main>
</body>
</html>
```